Floral Design for Weddings And Events

I create floral designs for weddings and events. I create unusual designs that people will remember.

Industry/Entity Type

Floral

Contact Information for Business Card

Petals
Weddings and Events
Marlene Hayward, owner/designer
3718 Delwood Ct
San Marcos, CA 92078
marlenehaywardq@mailvista.net
530 555-0172

Requirements
Must have
• I would like the name of the business, PETALS, to Stand Out!! I like clean, bold lines.. nothing foo-foo! Must be easy to read I'm looking for a design that catches your eye and represents my creativity. I want my card to show the potential customer that I'm unique and creative
Nice to have
• I'm thinking of the name PETALS maybe worked into the design... I'm open to your creative ideas!!!! The name must be very legible
Should not have
• I'm open to any colors other that pink and yellow..nothing Foo-Foo or flowery..

```html
<!DOCTYPE html>
<html lang="en">
<head>
<meta charset="utf-8">
<title>Petals Weddings and Events – Business Card</title>
<link rel="stylesheet" href="https://fonts.googleapis.com/css2?family=Arimo:wght@400;700&display=swap">
<style>
  :root {
    --backdrop: #d9d9d7;
    --card: #1c1b1b;
    --card-edge: #2a2828;
    --lime: #b5d334;
    --red: #e0282e;
    --white: #ffffff;
    --muted: #dcdcdc;
  }
  * { margin: 0; padding: 0; box-sizing: border-box; }
  html, body {
    width: 1200px;
    height: 692px;
    overflow: hidden;
    background: var(--backdrop);
    font-family: "Arimo", Arial, sans-serif;
  }
  .canvas {
    position: relative;
    width: 1200px;
    height: 692px;
  }
  .business-card {
    position: absolute;
    left: 180px;
    top: 106px;
    width: 840px;
    height: 480px;
    background: var(--card);
    border: 1px solid var(--card-edge);
    border-radius: 6px;
    box-shadow: 0 10px 30px rgba(0, 0, 0, 0.25);
    overflow: hidden;
    color: var(--white);
  }
  .owner {
    position: absolute;
    top: 44px;
    left: 400px;
  }
  .owner-name {
    font-size: 24px;
    font-weight: 400;
    letter-spacing: 0.2px;
  }
  .owner-role {
    margin-top: 6px;
    font-size: 15px;
    color: var(--muted);
  }
  .owner-role .accent { color: var(--red); }
  .brand {
    position: absolute;
    left: 0;
    right: 0;
    top: 150px;
    display: flex;
    align-items: center;
    justify-content: center;
    gap: 22px;
  }
  .brand-mark {
    width: 44px;
    height: 44px;
    border-radius: 50%;
    background: var(--lime);
  }
  .brand-name {
    font-size: 88px;
    font-weight: 400;
    line-height: 1;
    color: var(--white);
  }
  .details {
    position: absolute;
    left: 56px;
    top: 320px;
  }
  .tagline {
    font-size: 30px;
    font-weight: 400;
    margin-bottom: 14px;
  }
  .tagline .business { color: var(--red); }
  .contact {
    list-style: none;
    font-size: 21px;
    line-height: 1.35;
  }
</style>
</head>
<body>
  <main class="canvas">
    <section class="business-card" aria-label="Petals Weddings and Events business card">
      <div class="owner">
        <p class="owner-name">Marlene Hayward</p>
        <p class="owner-role">Owner/<span class="accent">designer</span></p>
      </div>

      <div class="brand">
        <span class="brand-mark" aria-hidden="true"></span>
        <p class="brand-name">Petals</p>
      </div>

      <div class="details">
        <p class="tagline"><span class="business">PETALS</span> Weddings and Events</p>
        <ul class="contact">
          <li>3718 Delwood Ct San Marcos, CA 92078</li>
          <li>530 555-0172</li>
          <li>marlenehaywardq@mailvista.net</li>
        </ul>
      </div>
    </section>
  </main>
</body>
</html>
```